Business Card for New Convenience Store

We need a business card for our new convenience store using our logo. We want to have a color scheme and back ground created that will be transferable to other media platforms and advertising.

Industry/Entity Type

Convenience Store

```html
<!DOCTYPE html>
<html lang="en">
<head>
<meta charset="utf-8">
<title>KMS Brenton – Business Card</title>
<link href="https://fonts.googleapis.com/css2?family=Open+Sans:wght@400;600;700;800&display=swap" rel="stylesheet">
<style>
  :root{
    --stage:#2b2b2b;
    --card-black:#050505;
    --card-white:#ffffff;
    --brand-red:#e3111b;
    --ink:#111111;
    --light-text:#f2f2f2;
    --divider:#8a8a8a;
    --photo-sky:#b9c4d6;
    --photo-stone:#8a6f55;
    --photo-ground:#d9d6d2;
  }
  *{box-sizing:border-box;margin:0;padding:0}
  html,body{width:1200px;height:1000px;overflow:hidden}
  body{
    background:var(--stage);
    font-family:"Open Sans",Arial,sans-serif;
    display:flex;flex-direction:column;align-items:center;justify-content:center;gap:60px;
  }
  .card{
    width:700px;height:400px;position:relative;overflow:hidden;
    background:var(--card-black);
    box-shadow:0 12px 30px rgba(0,0,0,.45);
  }

  /* ---------- front ---------- */
  .front__top{
    position:absolute;left:0;top:0;width:100%;height:182px;
    background:var(--card-white);
    border-bottom:12px solid var(--brand-red);
  }
  .brand{
    display:flex;align-items:center;gap:12px;
    font-weight:800;letter-spacing:1px;line-height:1;
  }
  .brand__dot{width:22px;height:22px;border-radius:50%;background:var(--brand-red);flex:none}
  .front .brand{
    position:absolute;left:50%;top:52px;transform:translateX(-50%);
    color:var(--ink);font-size:58px;white-space:nowrap;
  }
  .name-tab{
    position:absolute;left:50%;top:170px;transform:translateX(-50%);
    background:var(--brand-red);color:var(--card-white);
    padding:4px 22px 6px;font-size:17px;font-weight:700;white-space:nowrap;
  }
  .name-tab .role{font-weight:400}
  .name-tab .sep{opacity:.8;margin:0 6px;font-weight:400}
  .front__details{
    position:absolute;left:0;right:0;top:250px;
    display:flex;justify-content:center;align-items:center;gap:34px;
    color:var(--light-text);font-size:18px;line-height:1.65;
  }
  .address{text-align:right}
  .details-divider{width:1px;height:74px;background:var(--divider)}
  .contact-list{list-style:none}
  .contact-list li{display:flex;align-items:center;gap:12px}
  .contact-list svg{width:15px;height:15px;fill:none;stroke:var(--brand-red);stroke-width:2}
  .contact-list .icon-phone{fill:var(--brand-red);stroke:none}

  /* ---------- back ---------- */
  .back__photo{
    position:absolute;left:0;top:0;width:100%;height:236px;
    background:linear-gradient(180deg,var(--photo-sky) 0%,#d7dde6 35%,var(--photo-stone) 62%,var(--photo-ground) 100%);
  }
  .back__band{
    position:absolute;left:0;top:236px;width:100%;height:12px;background:var(--brand-red);
  }
  .back .brand{
    position:absolute;right:46px;top:290px;
    color:var(--card-white);font-size:56px;white-space:nowrap;
  }
</style>
</head>
<body>

  <section class="card front" aria-label="Business card front">
    <div class="front__top"></div>
    <div class="brand"><span class="brand__dot"></span>KMS BRENTON</div>
    <div class="name-tab">Dana Whitfield<span class="sep">|</span><span class="role">Manager</span></div>
    <div class="front__details">
      <address class="address" style="font-style:normal">42 Cedar Bend Rd.<br>Harlow Springs, AL 36000</address>
      <span class="details-divider"></span>
      <ul class="contact-list">
        <li>
          <svg viewBox="0 0 16 16" aria-hidden="true"><path class="icon-phone" d="M4 1h8a1 1 0 0 1 1 1v12a1 1 0 0 1-1 1H4a1 1 0 0 1-1-1V2a1 1 0 0 1 1-1zm1 2v8h6V3z"/></svg>
          555-014-2290
        </li>
        <li>
          <svg viewBox="0 0 16 16" aria-hidden="true"><rect x="1.5" y="3.5" width="13" height="9"/><path d="M1.5 3.5 8 9l6.5-5.5"/></svg>
          dwhitfield@kmsmart.com
        </li>
      </ul>
    </div>
  </section>

  <section class="card back" aria-label="Business card back">
    <div class="back__photo" role="img" aria-label="Photograph of the store building with stone walls, glass front and shoppers under a blue sky"></div>
    <div class="back__band"></div>
    <div class="brand"><span class="brand__dot"></span>KMS BRENTON</div>
  </section>

</body>
</html>
```